FB and Youtube banner design for HVAC company

I would like an appealing site page banner for business page on Facebook (851w x 315h pixels) and one for youtube (2560w x 1440h pixels) for hvac company. Business card design and logo are attached. Company name is Bright Meadow Air Conditioning, Refrigeration, and Heating.

NOTE: I put the business cards and log up to see some of the artwork the company is using. It's not to replicate that in the banner images.

Target Market(s)

Interested business and homeowner visitors to Facebook business page and youtube channel page.

Industry/Entity Type

Hvac

Font styles to use
Sans Serif

Requirements
Must have
• See logo for color scheme.
Should not have
• This should not look like a business card. Think of what is typically the banner on a facebook business page and youtube channel.

```html
<!DOCTYPE html>
<html lang="en">
<head>
<meta charset="utf-8">
<title>Bright Meadow – Social Banners</title>
<link rel="stylesheet" href="https://fonts.googleapis.com/css2?family=Source+Sans+3:wght@400;600;700&display=swap">
<style>
  :root {
    --page: #e4e6e9;
    --blue: #2b50a3;
    --blue-deep: #1f3f86;
    --orange: #f26a1b;
    --white: #ffffff;
  }
  * { margin: 0; padding: 0; box-sizing: border-box; }
  html, body { width: 1200px; height: 1200px; overflow: hidden; }
  body {
    background: var(--page);
    font-family: "Source Sans 3", "Helvetica Neue", Arial, sans-serif;
    position: relative;
  }
  .banner {
    position: absolute;
    background: var(--blue);
    overflow: hidden;
    color: var(--white);
  }
  .banner--facebook { left: 131px; top: 72px; width: 937px; height: 346px; }
  .banner--youtube  { left: 72px; top: 503px; width: 1056px; height: 593px; }

  .texture {
    position: absolute; left: 0; top: 0; bottom: 0;
    background: linear-gradient(90deg, var(--blue-deep) 0%, rgba(31,63,134,0.55) 30%, rgba(43,80,163,0) 62%);
  }
  .banner--facebook .texture { width: 520px; }
  .banner--youtube .texture { width: 620px; }

  .art { position: absolute; inset: 0; }

  .company {
    position: absolute;
    display: inline-block;
    font-weight: 700;
    line-height: 1;
    white-space: nowrap;
  }
  .company-name {
    display: block;
    text-transform: uppercase;
    letter-spacing: 0.3px;
    border-bottom: 2px solid var(--white);
    padding-bottom: 4px;
  }
  .company-services {
    display: block; font-weight: 600;
    font-variant: small-caps; letter-spacing: 0.4px; margin-top: 7px;
  }
  .banner--facebook .company { left: 65px; top: 38px; }
  .banner--facebook .company-name { font-size: 52px; }
  .banner--facebook .company-services { font-size: 20px; }
  .banner--youtube .company { left: 84px; top: 140px; }
  .banner--youtube .company-name { font-size: 56px; }
  .banner--youtube .company-services { font-size: 21px; }

  .reach {
    position: absolute; display: flex; gap: 18px; align-items: center;
    font-size: 13px; white-space: nowrap;
  }
  .reach-item { display: flex; align-items: center; gap: 5px; }
  .reach-item svg { width: 14px; height: 14px; }
  .banner--facebook .reach { left: 22px; top: 312px; }
  .banner--youtube .reach { left: 36px; top: 430px; font-size: 15px; gap: 22px; }
  .banner--youtube .reach-item svg { width: 16px; height: 16px; }

  .brand-mark {
    position: absolute; display: flex; align-items: center; justify-content: center;
    text-align: center; color: var(--blue); font-weight: 700;
    text-transform: uppercase; line-height: 0.95;
  }
  .banner--facebook .brand-mark { left: 623px; top: 34px; width: 280px; height: 280px; font-size: 44px; }
  .banner--youtube .brand-mark { left: 708px; top: 143px; width: 300px; height: 300px; font-size: 48px; }
</style>
</head>
<body>

<section class="banner banner--facebook" aria-label="Facebook cover banner">
  <div class="texture" role="img" aria-label="Triangle pattern backdrop fading from left"></div>
  <svg class="art" width="937" height="346" viewBox="0 0 937 346" aria-hidden="true">
    <circle cx="566" cy="73" r="18" fill="var(--orange)"/>
    <circle cx="524" cy="146" r="26" fill="var(--orange)"/>
    <circle cx="566" cy="246" r="38" fill="var(--orange)"/>
    <circle cx="763" cy="174" r="143" fill="var(--white)" stroke="var(--orange)" stroke-width="14"/>
  </svg>
  <h1 class="company">
    <span class="company-name">Bright Meadow</span>
    <span class="company-services">Air Conditioning, Refrigeration, and Heating</span>
  </h1>
  <div class="reach">
    <span class="reach-item"><svg viewBox="0 0 16 16"><path d="M4 1l3 3-2 2c1 2 3 4 5 5l2-2 3 3-2 2C7 14 2 9 2 3z" fill="var(--orange)"/></svg>555.301.0492</span>
    <span class="reach-item"><svg viewBox="0 0 16 16"><path d="M8 1l7 6h-2v8H3V7H1z" fill="var(--orange)"/></svg>INFO@BRIGHTMEADOWHVAC.COM</span>
    <span class="reach-item"><svg viewBox="0 0 16 16"><circle cx="8" cy="8" r="6.5" fill="none" stroke="var(--orange)" stroke-width="1.6"/><path d="M1.5 8h13M8 1.5c-3 3.5-3 9.5 0 13M8 1.5c3 3.5 3 9.5 0 13" fill="none" stroke="var(--orange)" stroke-width="1.2"/></svg>WWW.BRIGHTMEADOWHVAC.COM</span>
  </div>
  <div class="brand-mark">Bright<br>Meadow</div>
</section>

<section class="banner banner--youtube" aria-label="YouTube channel banner">
  <div class="texture" role="img" aria-label="Triangle pattern backdrop fading from left"></div>
  <svg class="art" width="1056" height="593" viewBox="0 0 1056 593" aria-hidden="true">
    <circle cx="644" cy="191" r="19" fill="var(--orange)"/>
    <circle cx="595" cy="268" r="29" fill="var(--orange)"/>
    <circle cx="644" cy="377" r="41" fill="var(--orange)"/>
    <circle cx="858" cy="293" r="152" fill="var(--white)" stroke="var(--orange)" stroke-width="15"/>
  </svg>
  <h2 class="company">
    <span class="company-name">Bright Meadow</span>
    <span class="company-services">Air Conditioning, Refrigeration, and Heating</span>
  </h2>
  <div class="reach">
    <span class="reach-item"><svg viewBox="0 0 16 16"><path d="M4 1l3 3-2 2c1 2 3 4 5 5l2-2 3 3-2 2C7 14 2 9 2 3z" fill="var(--orange)"/></svg>555.301.0492</span>
    <span class="reach-item"><svg viewBox="0 0 16 16"><path d="M8 1l7 6h-2v8H3V7H1z" fill="var(--orange)"/></svg>INFO@BRIGHTMEADOWHVAC.COM</span>
    <span class="reach-item"><svg viewBox="0 0 16 16"><circle cx="8" cy="8" r="6.5" fill="none" stroke="var(--orange)" stroke-width="1.6"/><path d="M1.5 8h13M8 1.5c-3 3.5-3 9.5 0 13M8 1.5c3 3.5 3 9.5 0 13" fill="none" stroke="var(--orange)" stroke-width="1.2"/></svg>WWW.BRIGHTMEADOWHVAC.COM</span>
  </div>
  <div class="brand-mark">Bright<br>Meadow</div>
</section>

</body>
</html>
```